Business Card Design for New Game Studio

We need a business card design. We are a new company developing innovative mobile and platform games.

I would like to see very innovative design thats brings out the company's goal and direction.

My Company's goal and direction is to "Evolve the way of gaming, Bring fun and entertainment to all gamers"

Please do use our company logo which I have attached to be included in the design.

Please put in details for name, title, contacts etc ... be creative !!!

Reason: Company logo redesign. Awaiting it. Thanks

Hi all Please do wait for my updated company logo. Thanks

Reason: Still waiting on new company logo. Thanks all

Hi All Designers .... Sorry for the long wait... Please see the new file for my new company logo uploaded. Waiting to see all your creative design. Cheers

Hi All .... Please do not just mass send a whole bunch of similar designs .... Would like to see quality instead of quantity Cheers

Entertainment

```html
<!DOCTYPE html>
<html lang="en">
<head>
<meta charset="utf-8">
<title>Verdant Realty – Business Card</title>
<link rel="stylesheet" href="https://fonts.googleapis.com/css2?family=Roboto+Condensed:wght@300;700&display=swap">
<style>
  :root {
    --canvas: #ffffff;
    --card-light: #ffffff;
    --card-dark: #414042;
    --card-border: #9a9a9a;
    --ink: #3a3a3c;
    --ink-soft: #4a4a4c;
    --accent: #d2df2a;
    --tagline: #ececec;
    --rule: #3f3f41;
  }
  * { margin: 0; padding: 0; box-sizing: border-box; }
  html, body {
    width: 1200px; height: 900px; overflow: hidden;
    background: var(--canvas);
    font-family: "Roboto Condensed", "Arial Narrow", sans-serif;
  }
  .canvas { position: relative; width: 1200px; height: 900px; }

  .card-front {
    position: absolute; left: 187px; top: 108px;
    width: 403px; height: 659px;
    background: var(--card-light);
    border: 1px solid var(--card-border);
  }
  .brand-block {
    position: absolute; left: 90px; top: -1px;
    width: 222px; height: 152px;
    background: var(--card-dark);
    display: flex; align-items: center; justify-content: center;
  }
  .brand-name {
    color: var(--accent); font-weight: 700; white-space: nowrap;
  }
  .brand-block .brand-name { font-size: 24px; }

  .contact, .address, .web {
    position: absolute; color: var(--ink-soft);
    font-size: 16px; font-weight: 300; line-height: 26px;
  }
  .contact { left: 72px; top: 226px; }
  .contact .person-name,
  .contact .person-title,
  .address .label {
    font-weight: 700; color: var(--ink);
  }
  .address { left: 67px; top: 364px; }
  .web { left: 67px; top: 523px; }

  .rule {
    position: absolute; left: 66px; width: 226px;
    height: 2px; background: var(--rule);
  }
  .rule-upper { top: 347px; }
  .rule-lower { top: 503px; }

  .card-back {
    position: absolute; left: 626px; top: 108px;
    width: 403px; height: 659px;
    background: var(--card-dark);
  }
  .back-brand {
    position: absolute; left: 0; right: 0; top: 272px;
    display: flex; align-items: center; justify-content: center; gap: 12px;
  }
  .back-brand .brand-mark {
    width: 26px; height: 26px; background: var(--accent);
  }
  .back-brand .brand-name { font-size: 34px; }
  .back-rule {
    position: absolute; left: 58px; top: 354px;
    width: 288px; height: 1px; background: var(--accent);
  }
  .tagline {
    position: absolute; left: 70px; width: 263px; top: 374px;
    text-align: center; color: var(--tagline);
    font-size: 16px; font-weight: 300; line-height: 26px;
  }
</style>
</head>
<body>
<main class="canvas">
  <section class="card-front">
    <div class="brand-block"><span class="brand-name">Verdant Realty</span></div>

    <div class="contact">
      <p class="person-name">NAME OF THE PERSON</p>
      <p class="person-title">DESIGNATION OF THE PERSON</p>
      <p>emailid@verdantrealty.com</p>
      <p>personal phone no</p>
    </div>
    <div class="rule rule-upper"></div>

    <div class="address">
      <p class="label">Address:</p>
      <p>type in number below</p>
      <p>street and road</p>
      <p>Area name, Place</p>
      <p>Pincode</p>
    </div>
    <div class="rule rule-lower"></div>

    <div class="web">
      <p>www.verdantrealty.com</p>
      <p>info@verdantrealty</p>
      <p>24hrs Helpline no</p>
    </div>
  </section>

  <section class="card-back">
    <div class="back-brand">
      <span class="brand-mark"></span>
      <span class="brand-name">Verdant Realty</span>
    </div>
    <div class="back-rule"></div>
    <p class="tagline">Evolve the way of gaming, Bring fun and entertainment to all gamersEvolve the way of gaming, Bring fun and entertainment to all gamers</p>
  </section>
</main>
</body>
</html>
```